KVRo Business Cards

We need a business card design. We are a Technology (Audio Visual) design, sales and installation company. Looking for a double sided design, clean

Contact Information for Business Card

Clean, modern look, 2 sided

Font styles to use
Sans Serif

```html
<!DOCTYPE html>
<html lang="en">
<head>
<meta charset="utf-8">
<title>KVRo Business Cards</title>
<link href="https://fonts.googleapis.com/css2?family=Montserrat:wght@500;600;700&family=Poppins:wght@400;500;700&display=swap" rel="stylesheet">
<style>
  :root {
    --stage: #2b2b2d;
    --navy: #1b3040;
    --navy-soft: #2a3f4f;
    --orange: #f6931e;
    --white: #ffffff;
    --ink: #1b3040;
    --rule: #5a6672;
  }
  * { box-sizing: border-box; margin: 0; padding: 0; }
  html, body { width: 1200px; height: 900px; overflow: hidden; }
  body {
    background: var(--stage);
    display: flex;
    flex-direction: column;
    align-items: center;
    justify-content: center;
    gap: 40px;
    font-family: "Poppins", sans-serif;
  }
  .card {
    position: relative;
    width: 640px;
    height: 366px;
    border-radius: 22px;
    overflow: hidden;
  }

  /* Front side */
  .card-front { background: var(--white); }
  .identity {
    position: absolute;
    left: 118px;
    top: 140px;
    font-family: "Montserrat", sans-serif;
  }
  .identity-name {
    color: var(--ink);
    font-weight: 700;
    font-size: 30px;
    letter-spacing: 0.5px;
    line-height: 1;
  }
  .identity-role {
    color: var(--orange);
    font-weight: 500;
    font-size: 17px;
    letter-spacing: 0.5px;
    margin-top: 6px;
    padding-left: 64px;
  }
  .divider {
    position: absolute;
    left: 352px;
    top: 92px;
    width: 1.5px;
    height: 150px;
    background: var(--rule);
  }
  .contact-list {
    position: absolute;
    left: 374px;
    top: 98px;
    list-style: none;
    font-size: 13.5px;
    color: var(--ink);
    line-height: 1.45;
  }
  .contact-list li { display: flex; align-items: flex-start; gap: 10px; }
  .contact-list svg { width: 14px; height: 14px; flex: none; margin-top: 3px; fill: var(--orange); }
  .contact-address { padding-left: 24px; }
  .front-band { position: absolute; left: 0; bottom: 0; width: 100%; height: 14px; }

  /* Back side */
  .card-back { background: var(--navy); }
  .backdrop-name {
    position: absolute;
    left: 30px;
    top: 30px;
    font-weight: 700;
    font-size: 250px;
    line-height: 1;
    color: var(--navy-soft);
    letter-spacing: -4px;
  }
  .brand-name {
    position: absolute;
    left: 0; right: 0;
    top: 118px;
    text-align: center;
    font-weight: 700;
    font-size: 78px;
    line-height: 1;
    color: var(--white);
    letter-spacing: 1px;
  }
  .tagline {
    position: absolute;
    left: 0; right: 0;
    bottom: 70px;
    text-align: center;
    font-weight: 500;
    font-size: 19px;
    color: var(--white);
    letter-spacing: 0.3px;
  }
</style>
</head>
<body>

<section class="card card-front" aria-label="Business card front">
  <div class="identity">
    <div class="identity-name">MARK DALTON</div>
    <div class="identity-role">CEO/FOUNDER</div>
  </div>
  <div class="divider"></div>
  <ul class="contact-list">
    <li>
      <svg viewBox="0 0 16 16" aria-hidden="true"><path d="M3.5 1.5l2.5 0 1 3.5-1.6 1.2a8 8 0 0 0 4.4 4.4l1.2-1.6 3.5 1v2.5c0 .8-.7 1.5-1.5 1.5A12.5 12.5 0 0 1 2 3c0-.8.7-1.5 1.5-1.5z"/></svg>
      <span>555 013 2480</span>
    </li>
    <li>
      <svg viewBox="0 0 16 16" aria-hidden="true"><path d="M4 1h8v4H4zM1 6h14v6h-3v3H4v-3H1zM5 10v4h6v-4z"/></svg>
      <span>555 013 2480</span>
    </li>
    <li>
      <svg viewBox="0 0 16 16" aria-hidden="true"><path d="M1 3h14v10H1zM2 4.2v.6l6 4 6-4v-.6z"/></svg>
      <span>info@kvro.com</span>
    </li>
    <li>
      <svg viewBox="0 0 16 16" aria-hidden="true"><path d="M8 1a7 7 0 1 0 0 14A7 7 0 0 0 8 1zm0 1.3c.8 0 1.8 1.7 2 4.2H6c.2-2.5 1.2-4.2 2-4.2zM2.4 7.5h2.3c0 1 .2 2 .4 2.8H3a5.7 5.7 0 0 1-.6-2.8zm.1-1h2.3c.1-1 .3-1.9.6-2.7A5.7 5.7 0 0 0 2.5 6.5zm3.5 1h4c0 1-.2 2-.4 2.8H6.4C6.2 9.5 6 8.5 6 7.5zm5.3 0h2.3c0 1-.2 2-.6 2.8h-2.1c.2-.8.4-1.8.4-2.8zm2.2-1h-2.3c-.1-1-.3-1.9-.6-2.7a5.7 5.7 0 0 1 2.9 2.7zM6.7 11.3h2.6c-.4 1.4-.9 2.4-1.3 2.4s-.9-1-1.3-2.4z"/></svg>
      <span>www.kvro.com</span>
    </li>
    <li>
      <svg viewBox="0 0 16 16" aria-hidden="true"><path d="M8 1a5 5 0 0 0-5 5c0 3.5 5 9 5 9s5-5.5 5-9a5 5 0 0 0-5-5zm0 7a2 2 0 1 1 0-4 2 2 0 0 1 0 4z"/></svg>
      <span>118 Alder Street NW</span>
    </li>
    <li class="contact-address">Suite 210, Lakeview</li>
    <li class="contact-address">MI 49000</li>
  </ul>
  <svg class="front-band" viewBox="0 0 640 14" preserveAspectRatio="none" aria-hidden="true">
    <polygon points="0,0 360,0 346,14 0,14" fill="var(--navy)"/>
    <polygon points="360,0 640,0 640,14 346,14" fill="var(--orange)"/>
  </svg>
</section>

<section class="card card-back" aria-label="Business card back">
  <div class="backdrop-name" aria-hidden="true">KVRo</div>
  <div class="brand-name">KVRo</div>
  <p class="tagline">Technology design, sales and installation</p>
</section>

</body>
</html>
```